TLR Property - Business Cards

Looking for a business card & general letterhead, signage etc design for our new logo.

Colours:
000a20
0056a2
00b5ef
0088ce
68cef2

Fonts:
Poppins
Karla

Please keep look and feel of new brand - example in the zip package I sent.

```html
<!DOCTYPE html>
<html lang="en">
<head>
<meta charset="utf-8">
<title>TLR Property – Business Cards</title>
<link rel="stylesheet" href="https://fonts.googleapis.com/css2?family=Poppins:wght@500;600;700&family=Karla:wght@400;500&display=swap">
<style>
  :root {
    --ink-navy: #000a20;
    --card-dark: #0b1120;
    --brand-blue: #0056a2;
    --card-blue: #0757a6;
    --sky: #00b5ef;
    --mid-blue: #0088ce;
    --ice: #68cef2;
    --stage: #242424;
    --white: #ffffff;
  }
  * { box-sizing: border-box; margin: 0; padding: 0; }
  html, body { width: 1200px; height: 781px; overflow: hidden; background: var(--stage); }
  .canvas {
    position: relative; width: 1200px; height: 781px;
    display: flex; align-items: center; justify-content: center; gap: 40px;
  }
  .card {
    position: relative; width: 540px; height: 309px;
    border-radius: 22px; border: 3px solid var(--sky);
    overflow: hidden;
  }
  .card--back { background: var(--card-blue); }
  .card--front { background: var(--card-dark); }

  .back-wordmark {
    position: absolute; inset: 0;
    display: flex; align-items: center; justify-content: center;
    font-family: "Poppins", sans-serif; font-weight: 700; font-size: 62px;
    color: #1d4f94; letter-spacing: 1px;
  }

  .brand {
    position: absolute; left: 34px; top: 38px;
    display: flex; align-items: center; gap: 12px;
  }
  .brand__mark { width: 34px; height: 34px; background: var(--mid-blue); }
  .brand__name {
    font-family: "Poppins", sans-serif; font-weight: 700; font-size: 34px;
    color: var(--brand-blue); line-height: 1;
  }

  .person {
    position: absolute; right: 0; top: 40px;
    display: flex; align-items: stretch; gap: 12px;
  }
  .person__text { text-align: right; padding-top: 2px; }
  .person__name {
    font-family: "Poppins", sans-serif; font-weight: 600; font-size: 22px;
    color: var(--brand-blue); letter-spacing: 0.5px; line-height: 1.1;
  }
  .person__role {
    font-family: "Karla", sans-serif; font-size: 14px; color: var(--white);
    letter-spacing: 0.5px;
  }
  .person__bar { width: 14px; background: var(--brand-blue); }

  .address {
    position: absolute; left: 34px; top: 170px;
    font-family: "Karla", sans-serif; font-size: 15px; line-height: 1.35;
    color: var(--white); letter-spacing: 0.3px;
  }
  .contacts {
    position: absolute; left: 34px; bottom: 26px;
    list-style: none;
    font-family: "Karla", sans-serif; font-size: 15px; line-height: 1.45;
    color: var(--white); letter-spacing: 0.3px;
  }
  .contacts li { display: flex; align-items: center; gap: 8px; }
  .contacts svg { width: 13px; height: 13px; flex: none; }
</style>
</head>
<body>
<main class="canvas">
  <section class="card card--back" aria-label="Business card back">
    <div class="back-wordmark">TLR Property</div>
  </section>

  <section class="card card--front" aria-label="Business card front">
    <div class="brand">
      <span class="brand__mark"></span>
      <span class="brand__name">TLR Property</span>
    </div>

    <div class="person">
      <div class="person__text">
        <div class="person__name">DANIEL HART</div>
        <div class="person__role">Managing Director</div>
      </div>
      <span class="person__bar"></span>
    </div>

    <address class="address" style="font-style:normal">
      Your address, City<br>State, Zip 1234
    </address>

    <ul class="contacts">
      <li>
        <svg viewBox="0 0 16 16" aria-hidden="true"><path fill="var(--sky)" d="M3.6 1.2l2.3 2.9-1.3 1.8c.9 2 2.5 3.6 4.5 4.5l1.8-1.3 2.9 2.3-1.2 2.4C7.4 13.5 2.5 8.6 1.2 2.4z"/></svg>
        123 456 789
      </li>
      <li>
        <svg viewBox="0 0 16 16" aria-hidden="true"><rect x="1" y="3" width="14" height="10" rx="1.5" fill="var(--sky)"/><path d="M1.8 4l6.2 5 6.2-5" stroke="var(--card-dark)" stroke-width="1.4" fill="none"/></svg>
        info@yourgmail.com
      </li>
      <li>
        <svg viewBox="0 0 16 16" aria-hidden="true"><circle cx="8" cy="8" r="6.5" fill="none" stroke="var(--sky)" stroke-width="1.5"/><ellipse cx="8" cy="8" rx="2.8" ry="6.5" fill="none" stroke="var(--sky)" stroke-width="1.2"/><path d="M1.5 8h13" stroke="var(--sky)" stroke-width="1.2"/></svg>
        www.yourwebsite.com
      </li>
    </ul>
  </section>
</main>
</body>
</html>
```